Business Card: RW Office Partners - Your tidy answer finder

Business Name: RW Office Partners
Website: www.rwofficepartners.com.au
Email: marisol@rwofficepartners.com.au
Mobile: 61 487 902 346
Facebook: @rwofficepartners
Instrgram: @rwofficepartners

Brading Colours:
HEX
#986474
#ddccd3
#7a8498
#c9d8e4
#000000
#ffffff

Tag Line: Your organised problem solver

Link to DRAFT website:
https://helpdeskhub.sitebuilderx.com/rw-office-partners

About Page from the website:
My name is Marisol Bramwell, and I would love to assist you to become more productive in your day to day and achieve your business and personal goals.
My mission is to give you time, time to work on the important tasks of your business or to be able to spend more time with your family. I will take on the tasks you don’t have time for, don’t know well or simply don’t like to do.
I have an extensive background in Administration, Tender Coordination, Document Control, WHS and Quality Management working primarily in the Construction, Mining and Corporate World.
I am passionate about being organised, having order and making things in your life (and mine) easier! I love to watch something unfold and grow into something amazing! I am known for being the go-to problem solver, the organiser of all things, producing high standards of work even under pressure. I’m also a confident communicator, and I understand that you’re busy running your business.

Target Market(s)

Small to Medium Business who require assistance in their business by a virtual assistant.

Industry/Entity Type

Virtual Assistant

Contact Information for Business Card

Mobile: 61 487 902 346

Font styles to use
Sans Serif

Colors
ffffff

Requirements
Must have
• Branding Colours as outlined.
Contact Details as outlined.
Logo as provided.
Proper contact details - mobile, facebook, instragm, website.
Simple, Elegant, very clean looking.
Should not have
• Note cute with pictures.
Not too girly as still want to market to construction companies.

```html
<!DOCTYPE html>
<html lang="en">
<head>
<meta charset="utf-8">
<title>RW Office Partners – Business Card</title>
<link href="https://fonts.googleapis.com/css2?family=Montserrat:wght@500;600;700&family=Quicksand:wght@500;600&display=swap" rel="stylesheet">
<style>
  :root {
    --mauve: #986474;
    --mauve-light: #ddccd3;
    --slate: #7a8498;
    --sky: #c9d8e4;
    --ink: #000000;
    --paper: #ffffff;
    --stage: #e6e7ea;
  }
  * { box-sizing: border-box; margin: 0; padding: 0; }
  html, body {
    width: 1200px; height: 900px; overflow: hidden;
    background: var(--stage);
  }
  .canvas { position: relative; width: 1200px; height: 900px; }

  .card {
    position: absolute; left: 320px; width: 560px; height: 342px;
    box-shadow: 0 8px 24px rgba(0,0,0,.18);
    overflow: hidden;
  }
  .card--front { top: 90px; background: var(--paper); }
  .card--back { top: 468px; }

  /* front */
  .holder { position: absolute; left: 40px; top: 34px; }
  .holder__name {
    font-family: "Montserrat", sans-serif; font-weight: 700;
    font-size: 19px; letter-spacing: .5px; color: var(--slate);
  }
  .holder__role {
    font-family: "Quicksand", sans-serif; font-weight: 600;
    font-size: 13px; color: var(--mauve); margin-top: 2px;
  }
  .holder__rule {
    width: 22px; height: 3px; background: var(--mauve); margin-top: 6px;
  }

  .contacts {
    position: absolute; left: 40px; top: 168px;
    display: grid; grid-template-columns: 18px 1px auto;
    column-gap: 10px; row-gap: 4px; align-items: center;
  }
  .contacts__icon { width: 14px; height: 14px; color: var(--mauve); }
  .contacts__divider { grid-row: 1 / span 3; grid-column: 2; width: 1px; height: 62px; background: var(--mauve); }
  .contacts__text {
    grid-column: 3;
    font-family: "Quicksand", sans-serif; font-weight: 500;
    font-size: 13px; color: var(--slate);
  }

  .brand {
    position: absolute; left: 300px; top: 118px;
    display: flex; align-items: center; gap: 10px;
  }
  .brand__mark { width: 14px; height: 14px; background: var(--mauve); }
  .brand__name {
    font-family: "Montserrat", sans-serif; font-weight: 600;
    font-size: 24px; line-height: 1.05; color: var(--mauve);
  }

  .social {
    position: absolute; left: 330px; top: 222px;
    display: grid; grid-template-columns: 12px 1px auto;
    column-gap: 10px; row-gap: 4px; align-items: center;
  }
  .social__dot { width: 9px; height: 9px; border-radius: 50%; background: var(--mauve); }
  .social__divider { grid-row: 1 / span 2; grid-column: 2; width: 1px; height: 38px; background: var(--mauve); }
  .social__text {
    grid-column: 3;
    font-family: "Quicksand", sans-serif; font-weight: 500;
    font-size: 13px; color: var(--slate);
  }

  .tagline-band {
    position: absolute; left: 0; right: 0; bottom: 14px; height: 26px;
    background: var(--slate);
    display: flex; align-items: center; padding-left: 40px;
    font-family: "Quicksand", sans-serif; font-weight: 600;
    font-size: 12px; color: var(--paper);
  }

  /* back */
  .back-field {
    position: absolute; inset: 0;
    background: linear-gradient(160deg, var(--mauve) 0%, #8a7383 45%, var(--slate) 100%);
  }
  .back-brand {
    position: absolute; right: 40px; bottom: 40px;
    display: flex; align-items: center; gap: 10px;
  }
  .back-brand__mark { width: 14px; height: 14px; background: var(--ink); }
  .back-brand__name {
    font-family: "Montserrat", sans-serif; font-weight: 600;
    font-size: 22px; line-height: 1.05; color: var(--ink);
  }
</style>
</head>
<body>
<main class="canvas">

  <section class="card card--front" aria-label="Business card front">
    <div class="holder">
      <p class="holder__name">YOUR NAME HERE</p>
      <p class="holder__role">Managing Director</p>
      <div class="holder__rule"></div>
    </div>

    <div class="brand">
      <span class="brand__mark"></span>
      <span class="brand__name">RW Office<br>Partners</span>
    </div>

    <div class="contacts">
      <svg class="contacts__icon" viewBox="0 0 14 14" fill="none" stroke="currentColor" stroke-width="1.2">
        <rect x="3.5" y="1" width="7" height="12" rx="1"/><line x1="6" y1="11" x2="8" y2="11"/>
      </svg>
      <span class="contacts__divider"></span>
      <span class="contacts__text">61 487 902 346</span>

      <svg class="contacts__icon" viewBox="0 0 14 14" fill="currentColor">
        <path d="M1 3h12v8H1z"/><path d="M1 3l6 5 6-5" stroke="#fff" stroke-width="1" fill="none"/>
      </svg>
      <span class="contacts__text">marisol@rwofficepartners.com.au</span>

      <svg class="contacts__icon" viewBox="0 0 14 14" fill="none" stroke="currentColor" stroke-width="1.1">
        <circle cx="7" cy="7" r="5.8"/><ellipse cx="7" cy="7" rx="2.6" ry="5.8"/><line x1="1.2" y1="7" x2="12.8" y2="7"/>
      </svg>
      <span class="contacts__text">www.rwofficepartners.com.au</span>
    </div>

    <div class="social">
      <span class="social__dot"></span>
      <span class="social__divider"></span>
      <span class="social__text">rwofficepartners</span>
      <span class="social__dot"></span>
      <span class="social__text">@rwofficepartners</span>
    </div>

    <div class="tagline-band">Your tidy answer finder</div>
  </section>

  <section class="card card--back" aria-label="Business card back">
    <div class="back-field" role="img" aria-label="Mauve to slate gradient with a faint repeated brand-name pattern"></div>
    <div class="back-brand">
      <span class="back-brand__mark"></span>
      <span class="back-brand__name">RW Office<br>Partners</span>
    </div>
  </section>

</main>
</body>
</html>
```